Summit Basin Operators, Inc. Company Brochure

I would like someone to design a brochure that can be handed out to prospective clients. We are a full service water and wastewater operations company that provides services to Municipal Utility Districts and citys. I would like something that is catchy to the eye and reflects a company that prides itself on providing personal service to its clients. We need to revamp our website, that's next, but the website does have a description of our company and services offered. You can find that information at www.summitbasinoperators.example

```html
<!DOCTYPE html>
<html lang="en">
<head>
<meta charset="utf-8">
<title>Summit Basin Operators, Inc. — Brochure Cover</title>
<link href="https://fonts.googleapis.com/css2?family=Mulish:wght@600;700;800&display=swap" rel="stylesheet">
<style>
  :root {
    --page-bg: #efedee;
    --cream: #f7f4e5;
    --navy: #2c3e57;
    --orange: #f07c2e;
    --white: #ffffff;
    --mark-blue: #4a9be0;
    --water-light: #8aa6b8;
    --water-mid: #5a7f9b;
    --water-deep: #3b5f80;
  }
  * { margin: 0; padding: 0; box-sizing: border-box; }
  html, body {
    width: 1200px;
    height: 900px;
    overflow: hidden;
    background: var(--page-bg);
    font-family: "Mulish", "Century Gothic", sans-serif;
  }
  .cover-panel {
    position: absolute;
    left: 417px;
    top: 9px;
    width: 366px;
    height: 884px;
    background: var(--cream);
    overflow: hidden;
  }
  .water-photo {
    position: absolute;
    left: 0;
    top: 330px;
    width: 100%;
    height: 554px;
    background:
      radial-gradient(ellipse 60% 12% at 62% 12%, rgba(235,242,245,0.55), rgba(235,242,245,0) 70%),
      radial-gradient(ellipse 80% 18% at 45% 62%, rgba(170,190,200,0.45), rgba(170,190,200,0) 70%),
      linear-gradient(180deg,
        rgba(247,244,229,1) 0%,
        rgba(200,210,210,0.9) 6%,
        var(--water-mid) 12%,
        var(--water-deep) 28%,
        var(--water-mid) 48%,
        var(--water-light) 66%,
        var(--water-mid) 82%,
        var(--water-deep) 100%);
  }
  .brand {
    position: absolute;
    top: 158px;
    left: 0;
    width: 100%;
    text-align: center;
  }
  .brand-dot {
    display: block;
    width: 40px;
    height: 40px;
    margin: 0 auto 20px;
    border-radius: 50%;
    background: var(--mark-blue);
  }
  .brand-name {
    font-weight: 800;
    font-size: 25px;
    line-height: 33px;
    letter-spacing: 0.2px;
    color: var(--navy);
  }
  .tagline {
    position: absolute;
    top: 493px;
    left: 0;
    width: 100%;
    text-align: center;
    font-weight: 700;
    font-size: 16px;
    line-height: 20px;
    color: var(--white);
  }
  .tagline .highlight { color: var(--orange); }
</style>
</head>
<body>
  <main class="cover-panel">
    <div class="water-photo" role="img" aria-label="Close-up photograph of a blue water surface with a gentle wave and sparkling light"></div>
    <header class="brand">
      <span class="brand-dot"></span>
      <h1 class="brand-name">SUMMIT BASIN<br>OPERATORS INC</h1>
    </header>
    <p class="tagline">
      An Emerging<br>
      <span class="highlight">Water &amp; Waste Water</span><br>
      Utility Company
    </p>
  </main>
</body>
</html>
```